Business Brochure / White Paper

This white paper is a marketing document to showcase ourselves to other businesses (private hospitals and other premium healthcare providers). The document should consist of bold and beautiful graphics. As an example of the sort of thing that we mean, we have attached the "velmora sky lineage records" white paper. It should consist of several A4 pages.
The content for the white paper is attached. Note that the content document is only a scaffold for the white paper and the exact layout does not need to be followed (especially text boxes which have just been placed roughly). You are free to use your artistic license to move content around in order to make the document as catchy as possible.
We have also included graphics that we have purchased licenses to and that we encourage to be used as you see fit. Note that in some places we have added a note after two asterisks (i.e. **) when we would like you to add specific images/graphics.
All of the relevant documents and graphics/images to be used to make the white paper can be found at the below link:
https://www.filquarry.net/sh/zhtwmekbb41paxl/BBDN5K3TB8FWLPNTq1tGmeOWRc?dl=0
Feel free to ask any questions.
Good Luck!
Hi,
Thank you for your submissions so far.
Please use our dropbox link for an updated and much more specific brief on what we require in terms of content, layout, and components:
Please note that we must make a decision within 3 days' time.
Please also note that we cannot select a designer unless designs for ALL PAGES of the white paper are submitted.
Thank you and good luck!

```html
<!DOCTYPE html>
<html lang="en">
<head>
<meta charset="utf-8">
<title>Helixora – Personalised Health &amp; Wellness</title>
<link rel="stylesheet" href="https://fonts.googleapis.com/css2?family=Lato:wght@300;400;700;900&display=swap">
<style>
  :root {
    --backdrop: #ecebe8;
    --paper: #f3f3f3;
    --ink: #4a4a4a;
    --ink-soft: #6b6b6b;
    --brand-blue: #1f7fcf;
    --brand-teal: #17a07a;
    --brand-green: #63a846;
  }
  * { box-sizing: border-box; margin: 0; padding: 0; }
  html, body {
    width: 1200px; height: 804px; overflow: hidden;
    background: var(--backdrop);
    font-family: "Lato", sans-serif;
  }
  /* The supplied design shows the cover page only; it is drawn flat here. */
  .cover {
    position: absolute; left: 332px; top: 23px;
    width: 536px; height: 758px;
    background: var(--paper);
    box-shadow: 0 6px 24px rgba(0,0,0,.18);
  }
  .brand {
    position: absolute; top: 100px; left: 0; width: 100%;
    display: flex; justify-content: center;
  }
  .brand-row { display: flex; align-items: center; gap: 10px; }
  .brand-dot { width: 18px; height: 18px; border-radius: 50%; background: var(--brand-green); flex: none; }
  .brand-text { display: flex; flex-direction: column; align-items: flex-end; }
  .brand-name {
    font-size: 38px; font-weight: 700; color: var(--brand-blue);
    line-height: 1; letter-spacing: .3px;
  }
  .brand-tagline {
    margin-top: 2px; font-size: 10px; font-weight: 700; color: var(--brand-blue);
    white-space: nowrap;
  }
  .mosaic {
    position: absolute; top: 186px; left: 58px;
    display: grid; grid-template-columns: repeat(3, 136px); gap: 4px;
  }
  .tile { width: 136px; height: 136px; }
  .tile--blue { background: var(--brand-blue); }
  .tile--teal { background: var(--brand-teal); }
  .tile--green { background: var(--brand-green); }
  .photo--helix { background: linear-gradient(135deg, #1e4b5c, #3c7a8a 55%, #c9963a); }
  .photo--lab { background: linear-gradient(160deg, #dfe8ef, #9fbcd3); }
  .photo--chart { background: linear-gradient(160deg, #f2f5f8, #c9d6e2); }
  .photo--specimen { background: linear-gradient(160deg, #e4eef4, #a9c9dc); }
  .photo--consult { background: linear-gradient(160deg, #efece7, #cfc8bd); }
  .photo--strand { background: linear-gradient(160deg, #4f7ea6, #1f3f63); }
  .title {
    position: absolute; top: 620px; width: 100%; text-align: center;
    font-size: 28px; font-weight: 900; color: var(--ink); letter-spacing: .3px;
    line-height: 1.2;
  }
  .subtitle {
    position: absolute; top: 672px; width: 100%; text-align: center;
    font-size: 16px; font-weight: 300; color: var(--ink-soft); line-height: 1.2;
  }
</style>
</head>
<body>
  <main class="cover">
    <header class="brand">
      <div class="brand-row">
        <span class="brand-dot"></span>
        <div class="brand-text">
          <span class="brand-name">helixora</span>
          <span class="brand-tagline">Personalised Health &amp; Wellness</span>
        </div>
      </div>
    </header>

    <section class="mosaic">
      <div class="tile photo--helix" role="img" aria-label="Close-up of a glowing DNA helix"></div>
      <div class="tile photo--lab" role="img" aria-label="Scientist working in a laboratory"></div>
      <div class="tile tile--blue"></div>
      <div class="tile tile--teal"></div>
      <div class="tile photo--chart" role="img" aria-label="Hand drawing a rising growth chart"></div>
      <div class="tile photo--specimen" role="img" aria-label="Researcher examining a DNA sample vial"></div>
      <div class="tile photo--consult" role="img" aria-label="Doctor shaking hands with a senior patient"></div>
      <div class="tile photo--strand" role="img" aria-label="Figure standing before a large DNA strand"></div>
      <div class="tile tile--green"></div>
    </section>

    <h1 class="title">HELIXORA</h1>
    <p class="subtitle">Personalised Health &amp; Wellness</p>
  </main>
</body>
</html>
```